People Analytics Company needs Web Design and CSS

We need a refreshed design for a People Analytics company called VOMTA Systems Inc. We have developed an online survey tool that our immediate need is to make it look snazzier for upcoming pilots with prospective companies. Dark Blue and Orange are the colors we like to use but the survey should be "neutral" - we don't want to influence any responses based on colors.

Target Market(s)

Enterprise Users

Industry/Entity Type

It Company

Coding

Coded - Design and coding required

Number of Pages Required

3 page

Font styles to use
Sans Serif

Colors
0556a4
f37122

Requirements
Must have
• User friendly way of responding to survey questions that is suitable for a tablet (fat fingers). Drag and Drop is also very hard on tablet.
• Neutral look and feel to reduce any potential respondent bias.
• Colors consistent with brand colors attached in document.
• Minimal scrolling is best.
Should not have
• Too many colors.

```html
<!DOCTYPE html>
<html lang="en">
<head>
<meta charset="utf-8">
<title>VOMTA Systems Inc. – Survey</title>
<link href="https://fonts.googleapis.com/css2?family=Roboto:ital,wght@0,300;0,400;0,500;0,700;1,300&display=swap" rel="stylesheet">
<style>
:root{
  --blue:#2f6fb4;
  --blue-dark:#0b4f9c;
  --navy:#0c2250;
  --orange:#e97318;
  --orange-deep:#c85d0a;
  --page:#f6f6f6;
  --grid:#e3e3e3;
  --text-muted:#8a8a8a;
  --footer:#333333;
}
*{box-sizing:border-box;margin:0;padding:0}
html,body{width:1200px;height:999px;overflow:hidden;background:var(--page);font-family:"Roboto",Arial,sans-serif}
.site-header{position:absolute;left:0;top:0;width:1200px;height:123px;background:#fff;border-top:3px solid var(--orange);box-shadow:0 1px 2px rgba(0,0,0,.05)}
.brand{position:absolute;left:99px;top:24px;display:flex;align-items:center;gap:10px}
.brand-dot{width:42px;height:42px;border-radius:50%;background:var(--navy)}
.brand-name{font-size:34px;font-weight:700;color:var(--navy);letter-spacing:1px;line-height:1}
.brand-name small{display:block;font-size:14px;font-weight:400;letter-spacing:0;margin-top:3px}
.main-nav{position:absolute;top:50px;left:477px;display:flex;font-size:13px;color:#777}
.main-nav a{color:inherit;text-decoration:none;margin-right:64px}
.main-nav a:nth-child(2){margin-right:64px}
.btn{position:absolute;top:50px;height:39px;line-height:39px;color:#fff;font-size:16px;text-align:center;border-radius:2px}
.btn-signin{left:865px;width:98px;background:var(--orange)}
.btn-start{left:969px;width:132px;background:var(--blue-dark)}

.survey{position:absolute;left:98px;top:153px;width:1002px;border-collapse:collapse;background:#fbfbfb}
.survey th{height:59px;background:linear-gradient(#f08a26,var(--orange-deep));color:#fff;text-align:left;font-weight:400;padding:0 0 0 15px;font-size:12.5px;line-height:1.4;border-right:1px solid #fff}
.survey th b{display:block;font-size:16px;font-weight:500}
.survey td{height:83px;border:1px solid var(--grid);text-align:center;vertical-align:middle}
.survey td.label{text-align:left;padding:0 8px 0 11px;font-size:11px;line-height:1.75;color:var(--text-muted)}
.survey td.label u{font-size:13px;color:#777}
.survey td.label.on{background:var(--blue);color:#fff;border-color:var(--blue)}
.survey td.label.on u{color:#fff}
.survey td.label.hot{background:var(--orange-deep);color:#fff;outline:2px solid #b75205;outline-offset:-2px}
.survey td.label.hot u{color:#fff}
.radio{display:inline-block;width:15px;height:15px;border:1px solid #d0d0d0;border-radius:50%;background:#fff}
.choice{background:var(--blue);color:#fff;font-style:italic;font-weight:300;font-size:13px}
.choice.hot{background:var(--orange-deep);outline:2px solid #b75205;outline-offset:-2px}

.btn-continue{position:absolute;left:963px;top:823px;width:137px;height:41px;line-height:39px;background:var(--blue-dark);color:#fff;font-size:20px;text-align:center;border:1px solid #08407f}

.site-footer{position:absolute;left:0;top:898px;width:1200px;height:101px;background:var(--footer);color:#fff}
.copyright{position:absolute;left:100px;top:50px;font-size:11px}
.social{position:absolute;left:931px;top:37px;display:flex;gap:6px}
.social span{width:29px;height:29px;border-radius:50%;background:#5a5a5a}
.page-code{position:absolute;right:71px;bottom:12px;font-size:10px}
</style>
</head>
<body>
<header class="site-header">
  <div class="brand"><span class="brand-dot"></span><span class="brand-name">VOMTA<small>Systems Inc.</small></span></div>
  <nav class="main-nav"><a href="#">HOME</a><a href="#">OUR PHILOSOPHY</a><a href="#">WHO WE ARE</a></nav>
  <a class="btn btn-signin">SIGN IN</a>
  <a class="btn btn-start">GET STARTED</a>
</header>

<table class="survey">
  <colgroup><col style="width:233px"><col style="width:147px"><col style="width:142px"><col style="width:149px"><col style="width:134px"><col style="width:197px"></colgroup>
  <thead><tr>
    <th></th>
    <th>LEFT STATMENT<b>MUCH BETTER</b></th>
    <th>LEFT STATEMENT<b>BETTER</b></th>
    <th>RIGHT STATEMENT<b>BETTER</b></th>
    <th>RIGHT STATEMENT<b>MUCH BETTER</b></th>
    <th></th>
  </tr></thead>
  <tbody>
    <tr><td class="label on"><u>THE COACH-</u>We continuously track and monitor the market on what people value effectiveness in different situations.</td>
      <td class="choice">Click Here</td><td><span class="radio"></span></td><td><span class="radio"></span></td><td><span class="radio"></span></td>
      <td class="label"><u>SINK OR SWIM-</u>We continuously track and monitor the market on in different situations.</td></tr>
    <tr><td class="label hot"><u>INSPIRATIONAL -</u>We continuously track monitor the market on what people value effectiveness in different situations.</td>
      <td><span class="radio"></span></td><td class="choice hot">Click Here</td><td><span class="radio"></span></td><td><span class="radio"></span></td>
      <td class="label"><u>FUNCTIONAL -</u>We continuously track and monitor the market on in different situations.</td></tr>
    <tr><td class="label"><u>DEMOCRATIC-</u>We continuously track &amp; monitor the market on what people value effectiveness in different situations.</td>
      <td><span class="radio"></span></td><td><span class="radio"></span></td><td class="choice">Click Here</td><td><span class="radio"></span></td>
      <td class="label on"><u>COMMANDING-</u>We continuously track and monitor the market on in different situations.</td></tr>
    <tr><td class="label"><u>HANDS ON-</u>We continuously track and monitor the market on what people value effectiveness in different situations.</td>
      <td><span class="radio"></span></td><td><span class="radio"></span></td><td><span class="radio"></span></td><td class="choice">Click Here</td>
      <td class="label on"><u>HANDS OFF-</u>We continuously track and monitor the market on in different situations.</td></tr>
    <tr><td class="label on"><u>BY THE BOOK-</u>We continuously track &amp; monitor the market on what people value effectiveness in different situations.</td>
      <td class="choice">Click Here</td><td><span class="radio"></span></td><td><span class="radio"></span></td><td><span class="radio"></span></td>
      <td class="label"><u>BURN THE BOOK-</u>We continsly track and monitor the market on in different situations.</td></tr>
    <tr><td class="label"><u>MASTER MANAGER-</u>We continuously monitor the market on what people value effectiveness in different situations.</td>
      <td><span class="radio"></span></td><td><span class="radio"></span></td><td class="choice">Click Here</td><td><span class="radio"></span></td>
      <td class="label on"><u>IN THETRENCHES-</u>We contintly track and monitor the market on in different situations.</td></tr>
    <tr><td class="label on"><u>EVEN KEEL-</u>We continuously track and monitor the market on what people value effectiveness in different situations.</td>
      <td><span class="radio"></span></td><td class="choice">Click Here</td><td><span class="radio"></span></td><td><span class="radio"></span></td>
      <td class="label"><u>HIGHS AND LOWS-</u>We continsly track and monitor the market on in different situations.</td></tr>
  </tbody>
</table>

<a class="btn-continue">Countinue &raquo;</a>

<footer class="site-footer">
  <p class="copyright">© Copy Right 2105 VOMTA.All copyrights Reserved.</p>
  <div class="social"><span></span><span></span><span></span><span></span><span></span></div>
  <span class="page-code">C2</span>
</footer>
</body>
</html>
```